Lawn Company needs design work on a service call flyer!

We are a lawn care company that fertilizes and sprays lawns. This design is meant to be left behind at the customers house after a lawn application has been done too let them know what we have done.

The finished design will be printed on A6 paper (4.1 x 5.8 inches)

I have attached PDF files of the text that I want on the front of the document and the back of the document. I also included a sample design that I had been working on to give some idea what I would like. I don't want the same design, but you can use it as a building block for something new or come up with something entirely different.

FRONT: The front of the design is most important.

BACK: Other then the text the design should be minimal. If possible I would like an outline of the trees in my logo to be a backdrop. I have attached a PDF of the back of my business card as an example

The winning design will be a professional looking document that flows and reflects a lawn care business. Please contact me if you have any questions. I will only pick a design that is better then my current template.

Thank You

Target Market(s)

Lawn Care Customers

Industry/Entity Type

Lawn Care

Requirements
Must have
• 1. Our Logo
• 2. The attached text for the front & back of document
• 3. Our phone number (604-918-4471)
• 4. Our Email address (fenwickturfcare@mailora.net)
Nice to have
• A green theme with flowing graphics
Should not have
• any pictures of houses, people, or tools
• Don't copy the text or design from my design template. It is outdated, is it meant to be an example only

```html
<!DOCTYPE html>
<html lang="en">
<head>
<meta charset="utf-8">
<title>Fenwick Turf Care – Service Card</title>
<link rel="stylesheet" href="https://fonts.googleapis.com/css2?family=Lato:wght@400;700;900&display=swap">
<style>
  :root {
    --paper: #f1f2f1;
    --green: #5bb52e;
    --green-deep: #1f6b2a;
    --ink: #1b1b1b;
    --white: #ffffff;
  }
  html, body {
    margin: 0;
    width: 1200px;
    height: 907px;
    overflow: hidden;
    background: var(--paper);
  }
  .card {
    position: relative;
    width: 1200px;
    height: 907px;
    overflow: hidden;
    font-family: "Lato", Arial, sans-serif;
    color: var(--ink);
  }
  .card-art {
    position: absolute;
    inset: 0;
  }
  .brand {
    position: absolute;
    left: 0;
    top: 100px;
    width: 330px;
    text-align: center;
    font-weight: 900;
    color: var(--green-deep);
    line-height: 1;
  }
  .brand-name { font-size: 44px; letter-spacing: 2px; display: block; }
  .brand-sub { font-size: 26px; letter-spacing: 2px; display: block; margin-top: 6px; }
  .line {
    position: absolute;
    margin: 0;
    font-size: 25px;
    line-height: 30px;
    white-space: nowrap;
  }
  .app-time { right: 36px; top: 288px; }
  .serviced-by { left: 41px; top: 350px; }
  .intro { left: 41px; top: 412px; }
  .treatment { left: 104px; }
  .treatment-fert { top: 460px; }
  .treatment-weed { top: 508px; }
  .treatment-other { top: 556px; }
  .watering { left: 41px; top: 630px; }
  .guarantee-title {
    position: absolute;
    left: 41px;
    top: 676px;
    margin: 0;
    font-size: 31px;
    line-height: 38px;
    font-weight: 700;
    letter-spacing: -0.5px;
  }
  .guarantee-text {
    position: absolute;
    left: 41px;
    top: 724px;
    width: 1118px;
    margin: 0;
    font-size: 21px;
    line-height: 31px;
    text-align: justify;
  }
  .contact {
    position: absolute;
    right: 40px;
    top: 866px;
    margin: 0;
    font-size: 19px;
    line-height: 24px;
    font-weight: 700;
    color: var(--white);
    white-space: nowrap;
  }
  .contact-sep { margin: 0 10px; }
</style>
</head>
<body>
<main class="card">
  <svg class="card-art" width="1200" height="907" viewBox="0 0 1200 907">
    <defs>
      <linearGradient id="paperTone" x1="0" y1="0" x2="1" y2="1">
        <stop offset="0" stop-color="#f7f7f7"/>
        <stop offset="0.6" stop-color="#e9eae9"/>
        <stop offset="1" stop-color="#d3d6d3"/>
      </linearGradient>
      <linearGradient id="grassTone" x1="0" y1="0" x2="1" y2="0">
        <stop offset="0" stop-color="#eef38a"/>
        <stop offset="0.45" stop-color="#dce83a"/>
        <stop offset="0.8" stop-color="#8cc63f"/>
        <stop offset="1" stop-color="#2f8a33"/>
      </linearGradient>
      <linearGradient id="swoosh" x1="0" y1="0" x2="1" y2="0">
        <stop offset="0" stop-color="#8cd13a"/>
        <stop offset="0.5" stop-color="#3f9f33"/>
        <stop offset="1" stop-color="#145a26"/>
      </linearGradient>
      <linearGradient id="swooshBottom" x1="0" y1="0" x2="1" y2="0">
        <stop offset="0" stop-color="#7ccc2c"/>
        <stop offset="0.6" stop-color="#3a9a30"/>
        <stop offset="1" stop-color="#1b6b28"/>
      </linearGradient>
    </defs>

    <rect width="1200" height="907" fill="url(#paperTone)" role="img" aria-label="Soft grey backdrop of dewy grass blades"/>

    <path d="M300 0 H1200 V0 C1050 120 750 150 360 150 Z" fill="url(#grassTone)" role="img" aria-label="Sunlit green grass close-up"/>
    <path d="M340 150 C700 160 1000 110 1200 0 V30 C1040 150 720 200 330 172 Z" fill="url(#swoosh)"/>

    <path d="M480 907 C700 862 950 842 1200 846 V907 Z" fill="url(#swooshBottom)"/>

    <circle cx="168" cy="72" r="182" fill="#ffffff"/>
    <path d="M8 150 A182 182 0 0 0 320 170" fill="none" stroke="#5bb52e" stroke-width="8"/>
  </svg>

  <div class="brand">
    <span class="brand-name">FENWICK</span>
    <span class="brand-sub">TURF CARE</span>
  </div>

  <p class="line app-time">APPLICATION TIME / DATE:_____________</p>
  <p class="line serviced-by">YOUR LAWN HAS BEEN PROFFESIONALLY SERVICED TODAY BY_______________________</p>
  <p class="line intro">Today's application consists of</p>
  <p class="line treatment treatment-fert">Seasonally Balanced Slow Release Fertilizer</p>
  <p class="line treatment treatment-weed">Broadleaf Weed Control (Please keep off the lawn until it is thoroughly dry)</p>
  <p class="line treatment treatment-other">Other _____________</p>
  <p class="line watering">Please begin watering the lawn __________________ after application</p>

  <h2 class="guarantee-title">Our Guarantee</h2>
  <p class="guarantee-text">“We strive to complete work in a professional manner each and every visit. If you are not satisfied with the level of service you are receiving please contact us. We value your business and wish to maintain long-term relationships with our customers.“</p>

  <p class="contact">604-918-4471<span class="contact-sep">|</span>fenwickturfcare@mailora.net</p>
</main>
</body>
</html>
```